Valtora

Standard Business Card design.
Sample two-sided design uploaded. White front, Black back.
Would like white shield to be on all black background side.
Willing to look at a couple creative designs, but nothing crazy.
Preference for a classic, confident, strong design.

```html
<!DOCTYPE html>
<html lang="en">
<head>
<meta charset="utf-8">
<title>Valtora Business Card</title>
<link href="https://fonts.googleapis.com/css2?family=Montserrat:wght@400;500;700;800&display=swap" rel="stylesheet">
<style>
  :root{
    --ink:#0b0b0b;
    --paper:#ffffff;
    --stage-top:#d4d4d4;
    --stage-bottom:#b9b9b9;
    --muted:#e6e6e6;
  }
  *{box-sizing:border-box;margin:0;padding:0}
  html,body{width:1200px;height:815px;overflow:hidden}
  body{
    background:linear-gradient(180deg,var(--stage-top),var(--stage-bottom));
    font-family:"Montserrat",Arial,sans-serif;
    position:relative;
  }
  .card{
    position:absolute;
    top:258px;
    width:525px;height:300px;
    border-radius:26px;
    background:var(--ink);
    overflow:hidden;
    box-shadow:0 14px 30px rgba(0,0,0,.28);
  }
  .card--front{left:50px}
  .card--back{left:625px}

  /* front */
  .front-disc{
    position:absolute;
    width:330px;height:330px;border-radius:50%;
    right:-70px;top:-120px;
    background:var(--paper);
    display:flex;align-items:center;justify-content:center;
  }
  .front-ring{
    position:absolute;
    width:344px;height:344px;border-radius:50%;
    right:-84px;top:-112px;
    border:3px solid var(--paper);
  }
  .front-disc .brand-name{
    color:var(--ink);
    font-size:30px;font-weight:800;letter-spacing:4px;
    margin-top:70px;margin-right:40px;
  }
  .details{
    position:absolute;left:36px;top:60px;
    color:var(--paper);
  }
  .wordmark{
    font-size:34px;font-weight:500;letter-spacing:5px;line-height:1;
  }
  .wordmark-rule{
    width:210px;height:1px;background:var(--paper);margin:10px 0 18px;
  }
  .person-name{font-size:22px;font-weight:800;letter-spacing:1.5px}
  .person-title{font-size:12px;font-weight:500;letter-spacing:2px;margin-top:2px}
  .address{font-size:12.5px;line-height:1.45;margin-top:16px;color:var(--muted)}
  .contacts{list-style:none;margin-top:14px;font-size:12.5px;color:var(--muted)}
  .contacts li{display:flex;align-items:center;gap:9px;margin-bottom:6px}
  .contacts svg{width:12px;height:12px;flex:none;fill:var(--paper)}

  /* back */
  .card--back{display:flex;align-items:center;justify-content:center}
  .back-brand{display:flex;align-items:center;gap:14px;color:var(--paper)}
  .back-brand .dot{width:16px;height:16px;border-radius:50%;background:var(--paper)}
  .back-brand .brand-name{font-size:40px;font-weight:800;letter-spacing:6px}
</style>
</head>
<body>
  <section class="card card--front" aria-label="Business card front">
    <div class="front-ring"></div>
    <div class="front-disc"><span class="brand-name">VALTORA</span></div>
    <div class="details">
      <div class="wordmark">VALTORA</div>
      <div class="wordmark-rule"></div>
      <div class="person-name">DANIEL REYES</div>
      <div class="person-title">MANAGER</div>
      <p class="address">482 North Harbor Street 12<br>Lakeview, MN 55021</p>
      <ul class="contacts">
        <li><svg viewBox="0 0 24 24"><path d="M6.6 10.8a15 15 0 0 0 6.6 6.6l2.2-2.2c.3-.3.7-.4 1-.2 1.1.4 2.3.6 3.6.6.6 0 1 .4 1 1V20c0 .6-.4 1-1 1A17 17 0 0 1 3 4c0-.6.4-1 1-1h3.5c.6 0 1 .4 1 1 0 1.3.2 2.5.6 3.6.1.3 0 .7-.2 1z"/></svg>(555)210-4837</li>
        <li><svg viewBox="0 0 24 24"><path d="M2 5h20v14H2zm2 2v.5l8 5 8-5V7z"/></svg>hello@valtora.com</li>
        <li><svg viewBox="0 0 24 24"><path d="M12 2a10 10 0 1 0 0 20 10 10 0 0 0 0-20zm-1 2.1V8H7.3A8 8 0 0 1 11 4.1zm2 0A8 8 0 0 1 16.7 8H13zM4.6 10H11v4H4.6a8 8 0 0 1 0-4zm8.4 0h6.4a8 8 0 0 1 0 4H13zm-5.7 6H11v3.9A8 8 0 0 1 7.3 16zm5.7 0h3.7a8 8 0 0 1-3.7 3.9z"/></svg>www.valtora.com</li>
      </ul>
    </div>
  </section>

  <section class="card card--back" aria-label="Business card back">
    <div class="back-brand"><span class="dot"></span><span class="brand-name">VALTORA</span></div>
  </section>
</body>
</html>
```